High end business card design for custom homebuilding company

Looking for a high end business card design that is unique and elegant. Can use embossing, foil printing, laser die cutting, or any high end printing technique or high end paper. Will upload current design so you can see the logo and what we are using currently, but we want something more unique and elegant. I included our logo to help with design.

Target Market(s)

High end custom home buyers of $1.5 million plus homes. Also real estate developers of high end communities.

Industry/Entity Type

Business

Contact Information for Business Card

Double sided. We want something very elegant and expensive looking. We are looking to incorporate a combination of perhaps linen paper or a high end paper, with foil stamping or embossing/debossing to make the card look unique, but still elegant. We tend to use blacks and golds, but are open to any ideas. Looking for creative and unique design.

Colors

Designer to choose colors to be used in the design.

Requirements
Must have
• High end, elegant look. Can use foil, embossing, or high end papers like linen. We want to make the card unique and interesting, but elegant and expensive looking.
Nice to have
• I am including just some cards I saw that looked interesting for one reason or another. I like a clean elegant design and like both the clean white style, and the blacks. So not sure if we want a black design or white. Would like to see both.

```html
<!DOCTYPE html>
<html lang="en">
<head>
<meta charset="utf-8">
<title>Halvorsen Custom Homes – Business Card</title>
<link href="https://fonts.googleapis.com/css2?family=Raleway:wght@400;700&display=swap" rel="stylesheet">
<style>
  :root{
    --backdrop:#141414;
    --card:#1c1c1c;
    --card-edge:#262626;
    --silver:#b9b9b9;
    --silver-dim:#6f6f6f;
    --foil:#8a8a8a;
  }
  *{margin:0;padding:0;box-sizing:border-box}
  html,body{width:1200px;height:900px;overflow:hidden;background:var(--backdrop)}
  body{font-family:'Raleway',sans-serif;display:flex;align-items:center;justify-content:center;gap:40px}
  .card{
    width:540px;height:327px;border-radius:22px;position:relative;
    background:linear-gradient(160deg,#232323 0%,var(--card) 55%,#161616 100%);
    border:1px solid var(--card-edge);
  }
  .wordmark{display:flex;align-items:center;gap:12px;color:var(--foil);font-weight:700;letter-spacing:3px;text-transform:uppercase}
  .wordmark .dot{width:30px;height:30px;border-radius:50%;background:var(--foil)}
  .wordmark .name{line-height:1.1}
  .wordmark .name span{display:block}
  .wordmark .line-main{font-size:30px}
  .wordmark .line-sub{font-size:12px;letter-spacing:9px;margin-top:4px}

  /* back side */
  .card-back .wordmark{position:absolute;left:120px;top:110px}
  .card-back .site{position:absolute;left:0;right:0;bottom:62px;text-align:center;font-size:13px;color:var(--silver-dim);letter-spacing:.5px}
  .card-back .site b{color:var(--silver);font-weight:700}

  /* front side */
  .card-front .wordmark{position:absolute;right:32px;top:40px}
  .card-front .wordmark .line-main{font-size:22px}
  .card-front .wordmark .line-sub{font-size:9px;letter-spacing:6px}
  .card-front .wordmark .dot{width:22px;height:22px}
  .person{position:absolute;left:36px;top:132px}
  .person-name{font-size:26px;font-weight:700;color:var(--silver);letter-spacing:1px}
  .person-role{font-size:11px;color:var(--silver-dim);letter-spacing:1.5px;margin-top:2px}
  .contacts{position:absolute;left:36px;top:210px;display:grid;grid-template-columns:150px 1fr;row-gap:12px;column-gap:10px}
  .contact{display:flex;align-items:flex-start;gap:8px;font-size:11.5px;color:var(--silver-dim);line-height:1.35}
  .contact svg{flex:none;width:16px;height:16px}
  .contact.wide{grid-column:1 / span 1}
</style>
</head>
<body>

<section class="card card-back" aria-label="Card back">
  <div class="wordmark">
    <div class="dot"></div>
    <div class="name"><span class="line-main">Halvorsen</span><span class="line-sub">Custom Homes</span></div>
  </div>
  <p class="site">www.<b>halvorsencustomhome</b>.com.au</p>
</section>

<section class="card card-front" aria-label="Card front">
  <div class="wordmark">
    <div class="dot"></div>
    <div class="name"><span class="line-main">Halvorsen</span><span class="line-sub">Custom Homes</span></div>
  </div>

  <div class="person">
    <h1 class="person-name">DECLAN MARSH</h1>
    <p class="person-role">MANAGING DIRECTOR</p>
  </div>

  <div class="contacts">
    <div class="contact">
      <svg viewBox="0 0 16 16"><circle cx="8" cy="8" r="7.5" fill="#555"/><path d="M5.5 4.5l1.5 0 .7 2-1 .8a5 5 0 0 0 2 2l.8-1 2 .7v1.5c-3.5.3-6.3-2.5-6-6z" fill="#1c1c1c"/></svg>
      <span>000 52 17 43</span>
    </div>
    <div class="contact">
      <svg viewBox="0 0 16 16"><circle cx="8" cy="8" r="7.5" fill="#555"/><circle cx="8" cy="8" r="4" fill="none" stroke="#1c1c1c" stroke-width="1.2"/><path d="M4 8h8M8 4c-1.8 2.4-1.8 5.6 0 8M8 4c1.8 2.4 1.8 5.6 0 8" stroke="#1c1c1c" stroke-width="1" fill="none"/></svg>
      <span>www.halvorsencustomhome.com.au</span>
    </div>
    <div class="contact">
      <svg viewBox="0 0 16 16"><circle cx="8" cy="8" r="7.5" fill="#555"/><rect x="5.5" y="3.5" width="5" height="9" rx="1" fill="#1c1c1c"/></svg>
      <span>000 61 28 09</span>
    </div>
    <div class="contact">
      <svg viewBox="0 0 16 16"><circle cx="8" cy="8" r="7.5" fill="#555"/><rect x="4" y="5" width="8" height="6" fill="#1c1c1c"/><path d="M4 5l4 3.2L12 5" stroke="#555" stroke-width="1" fill="none"/></svg>
      <span>info@halvorsencustomhome.com.au</span>
    </div>
    <div class="contact wide" style="grid-column:1 / span 2">
      <svg viewBox="0 0 16 16"><circle cx="8" cy="8" r="7.5" fill="#555"/><path d="M8 3.5a3 3 0 0 1 3 3c0 2.2-3 5.5-3 5.5s-3-3.3-3-5.5a3 3 0 0 1 3-3z" fill="#1c1c1c"/><circle cx="8" cy="6.5" r="1" fill="#555"/></svg>
      <span>HALVORSEN CUSTOM HOMES<br>Unit 3 14-18 Ashby Street, Bayswater, WA 6053</span>
    </div>
  </div>
</section>

</body>
</html>
```